7' x 4' sign for a new multiunit residential mountain location**

Our mission is to build people their dream home through the use of professional and thoughtful design. We're a new developer, building a new and feature-filled fourplex, and need a brand and presence that generates interests and builds our brand. Our homes are professionally and thoughtfully designed - we agonize over the details so our homeowners don't have to once they move in.

We're constructing a new fourplex in downtown Kelowna, BC, Canada. The location is in the heart of the city's entertainment and cultural zones, is surrounded by mountains and a lake, and within an hour of over 100 wineries. "RIDGELINE" residents prize their time outdoors - boating, biking, hiking, skiing, and more. It's no wonder Kelowna is often cited as one of the most beautiful and desirable places to live in the world.

attachments - brand elements, rendering of the unit, feature sheet for each unit, and picture of the sign casing (7' wide and 4' long envelop - pic of sign frame attached).

Target Market(s)

Young professionals (age 30 to 45); Empty nestes (age 55+)

Font styles to use
Other font styles liked:
• Cordia New

Requirements
Must have
• Our tag line - Built with care

Presence - this is an unusual shape and large sign. It must create interest and build our brand.

```html
<!DOCTYPE html>
<html lang="en">
<head>
<meta charset="utf-8">
<title>Ridgeline Property Development – Site Sign</title>
<link rel="stylesheet" href="https://fonts.googleapis.com/css2?family=Questrial&display=swap">
<style>
  :root {
    --backdrop: #e6e6e6;
    --sign-white: #fbfbfb;
    --ink: #2b2b2b;
    --band: #2c2c2c;
    --orange: #f07f12;
    --sign-font: "Questrial", sans-serif;
  }
  html, body {
    margin: 0;
    padding: 0;
    width: 1200px;
    height: 2442px;
    overflow: hidden;
    background: var(--backdrop);
  }
  .canvas {
    position: relative;
    width: 1200px;
    height: 2442px;
  }
  .sign {
    position: absolute;
    left: 50px;
    top: 908px;
    width: 1100px;
    height: 626px;
    background: var(--sign-white);
    font-family: var(--sign-font);
    color: var(--ink);
    box-shadow: 0 6px 18px rgba(0,0,0,0.25);
  }
  .sign-frame {
    position: absolute;
    left: 25px;
    top: 25px;
    right: 25px;
    bottom: 75px;
    border: 4px solid var(--ink);
    border-bottom: none;
  }
  .brand-name {
    position: absolute;
    left: 0;
    right: 0;
    top: 168px;
    margin: 0;
    text-align: center;
    font-size: 98px;
    font-weight: 400;
    letter-spacing: 10px;
    line-height: 1;
    color: var(--ink);
  }
  .tagline {
    position: absolute;
    left: 0;
    right: 0;
    top: 280px;
    text-align: center;
    font-size: 17px;
    line-height: 1;
    color: var(--ink);
  }
  .company-line {
    position: absolute;
    left: 0;
    right: 0;
    top: 322px;
    margin: 0;
    text-align: center;
    font-size: 58px;
    font-weight: 400;
    letter-spacing: 3px;
    line-height: 1;
  }
  .contact-email {
    position: absolute;
    left: 62px;
    top: 455px;
    font-size: 35px;
    line-height: 1;
  }
  .licence-note {
    position: absolute;
    left: 62px;
    top: 494px;
    font-size: 21px;
    line-height: 1;
  }
  .contact-phone {
    position: absolute;
    right: 68px;
    top: 463px;
    font-size: 32px;
    line-height: 1;
  }
  .web-band {
    position: absolute;
    left: 0;
    right: 0;
    bottom: 0;
    height: 75px;
    background: var(--band);
    display: flex;
    align-items: center;
    justify-content: center;
  }
  .web-address {
    color: var(--orange);
    font-size: 32px;
    letter-spacing: 18px;
    margin-right: -18px;
  }
</style>
</head>
<body>
<main class="canvas">
  <section class="sign" aria-label="Ridgeline Property Development site sign">
    <div class="sign-frame"></div>

    <h1 class="brand-name">RIDGELINE</h1>
    <div class="tagline">Built with care</div>

    <h2 class="company-line">PROPERTY DEVELOPMENT LTD</h2>

    <div class="contact-email">j.harlow@ridgelinehomes.ca</div>
    <div class="licence-note">Licensed Residential Builder</div>
    <div class="contact-phone">PH: 250 555 0148</div>

    <div class="web-band">
      <span class="web-address">RIDGELINEPROPERTYDEV.COM</span>
    </div>
  </section>
</main>
</body>
</html>
```